ご覧いただきまして、有難うございます!

制作イメージなどの詳細を記載しております依頼書を以下URLからダウンロードしてご確認頂けますと幸いです。
(依頼書の格納フォルダ)
https://files.morvendale.net/share/folders/7QxT3pN8vLc2Hs5KdW9yRb4ZmE1uGoFaJ?mode=view

継続的にデザインの改修を予定しておりまして、継続的にページのデザイン制作をしていただける方を探しております。長期的な関係を築ければと思います。

上記URL先に格納しております依頼書をお読み頂き、ご質問等ありましたら、気軽にお問い合わせください。
たくさんのご応募をお待ちしております!
依頼書は以下格納フォルダからご確認をお願いします。
(依頼書の格納フォルダ)
• モバイルファースト・レスポンシブWebデザイン対応(モバイル用とPC用を納品)
緑系、青系
難しい要望とは認識しておりますが、良いものを作りたく、何卒よろしくお願いいたします。
ご覧いただきまして、有難うございます!

(依頼書の格納フォルダ)

たくさんのご応募をお待ちしております!

どれもとても良いFVでご提案ありがとうございます。
デザインイメージの中でも、ポジティブな、透明性のあるの2点が特徴的であったため、今回はこちらの提案を選ばせて下さい。

どれもとても良いFVのデザインのご提案ありがとうございます。
社内や外部でも感想を聞く中で、皆様の1つ1つのご提案が大変好評でした。

皆様、お忙しい中で数ある提案依頼がある中で、こちらへご提案を下さり大変感謝しております。次回の製作依頼の際も、ぜひ参加してもらえるとありがたいです。
どうもありがとうございました。

```html
<!DOCTYPE html>
<html lang="ja">
<head>
<meta charset="UTF-8">
<title>ハルカ塾 | 進学型の個別指導</title>
<link href="https://fonts.googleapis.com/css2?family=Noto+Sans+JP:wght@500;700;900&display=swap" rel="stylesheet">
<style>
:root{
  --green:#1f8a4c;
  --green-dark:#17733e;
  --green-pale:#e6f3ea;
  --ink:#222a26;
  --gray:#6b7370;
  --hero-bg:#f3f5f3;
  --yellow:#f7c928;
  --white:#ffffff;
}
*{margin:0;padding:0;box-sizing:border-box}
html,body{width:1200px;height:2360px;overflow:hidden;background:var(--white)}
body{font-family:"Noto Sans JP",sans-serif;color:var(--ink);position:relative}

.site-header{position:absolute;left:0;top:0;width:1200px;height:180px;display:flex;align-items:center;justify-content:space-between;padding:0 40px}
.brand{display:flex;align-items:center;gap:22px;font-weight:900;font-size:72px;color:var(--green);letter-spacing:4px}
.brand-mark{width:60px;height:60px;background:var(--green);border-radius:10px}
.btn-contact-sm{width:368px;height:96px;border-radius:48px;background:var(--green);color:var(--white);font-weight:700;font-size:40px;display:flex;align-items:center;justify-content:center;gap:28px}

.hero{position:absolute;left:0;top:180px;width:1200px;height:1360px;background:var(--hero-bg);overflow:hidden}
.hero-photo{position:absolute;left:660px;top:0;width:540px;height:1360px;background:linear-gradient(160deg,#cfd8d4 0%,#9fb0ab 40%,#3b4a5a 75%,#e9ece8 100%)}
.hero-deco{position:absolute;border-radius:50%;background:var(--green);opacity:.85}
.hero-copy{position:absolute;left:72px;top:100px;width:580px}
.lead{font-weight:900;font-size:64px;line-height:92px;color:var(--ink);white-space:nowrap}
.lead em,.title em{font-style:normal;color:var(--green)}
.title{margin-top:16px;font-weight:900;font-size:132px;line-height:160px;letter-spacing:1px;white-space:nowrap}
.badges{position:absolute;left:72px;top:640px;display:flex;flex-direction:column;gap:40px}
.badge{width:536px;height:140px;background:var(--yellow);font-weight:700;font-size:50px;line-height:62px;display:flex;flex-direction:column;justify-content:center;align-items:center;text-align:center}
.btn-contact{position:absolute;left:180px;top:1112px;width:832px;height:148px;border-radius:74px;background:var(--green);color:var(--white);font-weight:700;font-size:52px;display:flex;align-items:center;justify-content:center;box-shadow:0 10px 0 var(--green-dark)}
.btn-contact svg{position:absolute;right:64px}

.campaign{position:absolute;left:20px;top:1572px;width:1160px;height:288px;background:var(--green-pale);padding:40px 40px}
.campaign-label{font-weight:700;font-size:42px}
.campaign-offer{font-weight:700;font-size:40px;color:var(--green);margin-top:12px}
.campaign-note{font-weight:500;font-size:32px;color:var(--gray);margin-top:10px}
.btn-more{position:absolute;right:40px;top:86px;width:236px;height:84px;border:4px solid var(--green);border-radius:42px;background:var(--white);color:var(--green);font-weight:700;font-size:32px;display:flex;align-items:center;justify-content:center;gap:14px}

.reasons-heading{position:absolute;left:0;top:1960px;width:1200px;text-align:center;font-weight:900;font-size:68px}
.reasons-heading span{background:linear-gradient(transparent 62%,#c6e6d1 62%)}
.reason-tag{position:absolute;left:20px;top:2232px;writing-mode:vertical-rl;transform:rotate(180deg);font-weight:700;font-size:30px;letter-spacing:4px;color:var(--green);border-right:4px solid var(--green);padding-right:8px}
.reason-title{position:absolute;left:152px;top:2232px;font-weight:900;font-size:64px;line-height:96px}
</style>
</head>
<body>
<header class="site-header">
  <div class="brand"><span class="brand-mark"></span>ハルカ塾</div>
  <a class="btn-contact-sm">お問い合わせ
    <svg width="20" height="32" viewBox="0 0 20 32"><path d="M4 4l12 12L4 28" stroke="#fff" stroke-width="5" fill="none"/></svg></a>
</header>

<section class="hero">
  <div class="hero-photo" role="img" aria-label="制服姿の生徒と教室で学ぶ生徒たちの写真"></div>
  <span class="hero-deco" style="left:-60px;top:820px;width:160px;height:160px"></span>
  <span class="hero-deco" style="left:20px;top:930px;width:90px;height:90px;opacity:.6"></span>
  <span class="hero-deco" style="left:1130px;top:1040px;width:140px;height:140px;opacity:.5"></span>
  <div class="hero-copy">
    <p class="lead"><em>都立高校上位校</em>を<br>目指すなら</p>
    <h1 class="title"><em>進学型</em>の<br>個別指導</h1>
  </div>
  <div class="badges">
    <p class="badge"><span>5科目対応で</span><span>月額26,400円</span></p>
    <p class="badge"><span>91.4%の生徒が</span><span>+50点以上アップ</span></p>
  </div>
  <a class="btn-contact">お問い合わせ
    <svg width="22" height="36" viewBox="0 0 22 36"><path d="M4 4l14 14L4 32" stroke="#fff" stroke-width="5" fill="none"/></svg></a>
</section>

<aside class="campaign">
  <p class="campaign-label">新教室限定 新規開校特典</p>
  <p class="campaign-offer">入塾金無料＆教材プレゼント!</p>
  <p class="campaign-note">2022年に開校した教室限定の入会キャンペーンです。</p>
  <a class="btn-more">詳しく見る
    <svg width="14" height="22" viewBox="0 0 14 22"><path d="M3 3l8 8-8 8" stroke="#1f8a4c" stroke-width="4" fill="none"/></svg></a>
</aside>

<h2 class="reasons-heading"><span>ハルカ塾が選ばれる理由</span></h2>
<p class="reason-tag">REASON 1</p>
<h3 class="reason-title">都立入試に必要な5科目すべてを<br>受験レベルに引き上げる</h3>
</body>
</html>
```